Business card and email signature

I have an email signature and business which needs to incorporate 2 brand logos and a company name. It is very clumsy looking. It needs to be more streamlined and work well on mobile. The company name Fairway Crest Links Alliance should be the smallest of the 3 as the 2 brand names are important on emails. However the company name FCL Alliance gives us credibility so needs to be incorporated within the name/contact details area. No address is required- just mobile and email
On the business card the logo s on the rear would be TeeUpDrive and SeatHubLink. On the front would be contact details and the FCL Alliance logo as this is the important one in this case

```html
<!DOCTYPE html>
<html lang="en">
<head>
<meta charset="utf-8">
<title>Mara Ellison – Business Card</title>
<link rel="stylesheet" href="https://fonts.googleapis.com/css2?family=Outfit:wght@300;400;500;600&display=swap">
<style>
  :root {
    --paper: #ffffff;
    --ink: #283034;
    --rule: #a7a396;
    --icon: #948f86;
    --mark: #94948c;
    --arc: #e9e9e8;
    --dots: #eeeeee;
  }
  html, body {
    margin: 0;
    padding: 0;
    overflow: hidden;
    background: var(--paper);
  }
  .card {
    position: relative;
    width: 1200px;
    height: 667px;
    overflow: hidden;
    background: var(--paper);
    font-family: "Outfit", sans-serif;
    color: var(--ink);
  }
  .halftone-field {
    position: absolute;
    left: 0;
    top: 0;
    width: 1000px;
    height: 667px;
    background: radial-gradient(ellipse 70% 80% at 10% 25%, var(--dots) 0%, rgba(238,238,238,0.5) 45%, rgba(255,255,255,0) 75%);
  }
  .side-arc {
    position: absolute;
    left: 0;
    top: 0;
    width: 1200px;
    height: 667px;
  }
  .holder-name {
    position: absolute;
    left: 0;
    width: 1200px;
    top: 106px;
    margin: 0;
    text-align: center;
    font-size: 110px;
    font-weight: 400;
    letter-spacing: 1px;
    line-height: 1;
    padding-right: 5px;
    box-sizing: border-box;
  }
  .name-rule {
    position: absolute;
    left: 302px;
    top: 247px;
    width: 596px;
    height: 0;
    border-top: 2px solid var(--rule);
  }
  .contact-list {
    position: absolute;
    left: 310px;
    top: 312px;
    margin: 0;
    padding: 0;
    list-style: none;
  }
  .contact-item {
    display: flex;
    align-items: center;
    height: 50px;
    margin-bottom: 16px;
    font-size: 31px;
    font-weight: 300;
    letter-spacing: 0.3px;
  }
  .contact-icon {
    width: 50px;
    height: 50px;
    margin-right: 28px;
    flex: none;
  }
  .affiliations {
    position: absolute;
    left: 325px;
    top: 530px;
    height: 46px;
    display: flex;
    align-items: center;
    color: var(--mark);
  }
  .guild-name {
    font-size: 24px;
    font-weight: 600;
    width: 232px;
  }
  .divider {
    width: 0;
    height: 34px;
    border-left: 2px solid var(--mark);
    margin: 0 28px 0 6px;
  }
  .alliance-name {
    font-size: 36px;
    font-weight: 600;
    letter-spacing: 0.2px;
  }
</style>
</head>
<body>
<main class="card">
  <div class="halftone-field" role="img" aria-label="Faint grey halftone dot pattern fading out from the top left"></div>

  <svg class="side-arc" viewBox="0 0 1200 667" aria-hidden="true">
    <circle cx="1545" cy="335" r="505" fill="var(--arc)"/>
  </svg>

  <h1 class="holder-name">Mara Ellison</h1>
  <div class="name-rule"></div>

  <ul class="contact-list">
    <li class="contact-item">
      <svg class="contact-icon" viewBox="0 0 50 50" aria-hidden="true">
        <circle cx="25" cy="25" r="25" fill="var(--icon)"/>
        <path d="M17.5 13.5c1-.9 2.3-.8 3 .3l2.4 3.6c.6.9.4 2-.4 2.7l-1.6 1.3c1.2 2.9 3.6 5.6 6.5 7l1.4-1.6c.7-.8 1.9-.9 2.7-.3l3.5 2.5c1.1.8 1.2 2.1.3 3.1l-1.6 1.8c-1.4 1.5-3.6 2-5.6 1.2-7-2.9-12.1-8.4-14.4-15.2-.6-2 0-4.1 1.5-5.4z" fill="#ffffff"/>
      </svg>
      <span>07700 900418</span>
    </li>
    <li class="contact-item">
      <svg class="contact-icon" viewBox="0 0 50 50" aria-hidden="true">
        <circle cx="25" cy="25" r="25" fill="var(--icon)"/>
        <rect x="12.5" y="16" width="25" height="18" rx="2" fill="none" stroke="#ffffff" stroke-width="2.4"/>
        <path d="M13.5 17.5 25 26.5l11.5-9" fill="none" stroke="#ffffff" stroke-width="2.4" stroke-linejoin="round"/>
      </svg>
      <span>mara.ellison@fairwaycrest.co.uk</span>
    </li>
  </ul>

  <div class="affiliations">
    <span class="guild-name">Greenway Players Guild</span>
    <span class="divider"></span>
    <span class="alliance-name">FCL Alliance</span>
  </div>
</main>
</body>
</html>
```